Modern business card design for professional copywriter

I'd like a business card design that I can use to have my cards printed out by plink.com as a squared corners business card (see artwork and design guidelines here: https://help.plink.com/hc/en-gb/sections/300481726-PLINK-Product-Templates)

The design should be clean and modern and reflect the colours, tone and branding on my website: https://noravestrel.com.au

Target Market(s)

Professionals, B2B small business owners

Industry/Entity Type

Business

Contact Information for Business Card

Nora Vestrel
m: 0427 593 864
e: nora@noravestrel.com.au
w: noravestrel.com.au

Font styles to use
Sans Serif

Requirements
Must have
• Tagline: "Sharp copywriting for busy business owners"
• Brand colours: fd8000, 009984, 666666 and black
Nice to have

```html
<!DOCTYPE html>
<html lang="en">
<head>
<meta charset="utf-8">
<title>Nora Vestrel – Copywriter Business Card</title>
<link href="https://fonts.googleapis.com/css2?family=Jost:wght@400;500&display=swap" rel="stylesheet">
<style>
  :root {
    --teal: #139c87;
    --orange: #f07d1c;
    --white: #ffffff;
    --backdrop: #ece7df;
    --card-shadow: 0 6px 18px rgba(0, 0, 0, 0.28);
  }
  html, body {
    margin: 0;
    width: 1200px;
    height: 1000px;
    overflow: hidden;
    background: var(--backdrop);
    font-family: "Jost", "Futura", sans-serif;
  }
  .card {
    position: absolute;
    left: 295px;
    width: 586px;
    height: 334px;
    box-shadow: var(--card-shadow);
    overflow: hidden;
  }
  .card--front { top: 150px; background: var(--white); }
  .card--back { top: 517px; background: var(--teal); }

  .brand-name {
    position: absolute;
    left: 0;
    width: 100%;
    margin: 0;
    text-align: center;
    font-weight: 500;
    font-size: 40px;
    letter-spacing: -0.5px;
    line-height: 1;
  }
  .card--front .brand-name { top: 120px; color: var(--teal); }
  .card--back .brand-name { top: 155px; color: var(--white); }

  .accent-rule {
    position: absolute;
    left: 0;
    top: 232px;
    width: 100%;
    height: 4px;
    background: var(--orange);
  }
  .contact-band {
    position: absolute;
    left: 0;
    top: 238px;
    width: 100%;
    height: 96px;
    background: var(--teal);
    color: var(--white);
  }
  .identity {
    position: absolute;
    right: 313px;
    top: 20px;
    text-align: right;
    font-size: 19px;
    line-height: 22px;
    letter-spacing: 0.2px;
  }
  .divider {
    position: absolute;
    left: 295px;
    top: 21px;
    width: 1.5px;
    height: 54px;
    background: var(--white);
  }
  .contact-list {
    position: absolute;
    left: 316px;
    top: 18px;
    margin: 0;
    padding: 0;
    list-style: none;
    font-size: 15px;
    line-height: 20px;
    letter-spacing: 0.3px;
  }
  .contact-list li { display: flex; align-items: center; gap: 13px; }
  .contact-list svg { width: 11px; height: 11px; flex: none; }

  .tagline {
    position: absolute;
    left: 0;
    top: 288px;
    width: 100%;
    margin: 0;
    text-align: center;
    color: var(--white);
    font-size: 14px;
    line-height: 18px;
    font-weight: 500;
    letter-spacing: 0.4px;
  }
</style>
</head>
<body>
  <section class="card card--front">
    <div class="brand-name">Nora Vestrel</div>
    <div class="accent-rule"></div>
    <div class="contact-band">
      <div class="identity">Nora Vestrel<br>Copywriter</div>
      <div class="divider"></div>
      <ul class="contact-list">
        <li>
          <svg viewBox="0 0 10 10" aria-hidden="true"><rect x="2.5" y="0.5" width="5" height="9" rx="1" fill="none" stroke="#fff" stroke-width="1.2"/><rect x="4.3" y="7.4" width="1.4" height="0.9" fill="#fff"/></svg>
          0427 593 864
        </li>
        <li>
          <svg viewBox="0 0 10 10" aria-hidden="true"><rect x="0.5" y="2" width="9" height="6.5" fill="#fff"/><path d="M0.5 2.3 L5 5.6 L9.5 2.3" fill="none" stroke="#139c87" stroke-width="1"/></svg>
          nora@noravestrel.com.au
        </li>
        <li>
          <svg viewBox="0 0 10 10" aria-hidden="true"><circle cx="4" cy="4" r="3" fill="none" stroke="#fff" stroke-width="1.5"/><path d="M6.2 6.2 L9.3 9.3" stroke="#fff" stroke-width="1.8" stroke-linecap="round"/></svg>
          noravestrel.com.au
        </li>
      </ul>
    </div>
  </section>

  <section class="card card--back">
    <div class="brand-name">Nora Vestrel</div>
    <p class="tagline">Sharp copywriting for busy business owners</p>
  </section>
</body>
</html>
```